Vortrane Global Compounding Pharmacy needs a great Sales Brochure targeting doctors

We need a sales brochure that is catered to Physicians that will get their interest to use our services as a compounding pharmacy for their patients with the following--

Features: Vortrane is a compounding lab that provides customized solutions to doctors looking to improve the lives of their patients.

Advantages: We offer personalized service, quality products, and reliable pharmaceuticals.

Benefits: By working directly with us, we can create solutions that best meet your practice's needs.

The logo is provided as well as pictures and a design brief. Colors should reflect our site and be blue and/shades of blue

Design Brief has been uploaded as a PDF

Target Market(s)

Doctors

Industry/Entity Type

Healthcare Compounding Pharmacy

Colors
0054AA
0677BA
7BADD7
CADEEF
E8F1F8
0094D4
00A9DD
6FCCEA
C7EBF8
E9F6FB

Requirements
Must have
• This should be a bi-fold brochure Use the slogan from VORTRANE INTRO in the brief and highlight it. The doctors need to be focus on why Vortrane is the right choice as well from the ABOUT VORTRANE SECTION.
Nice to have
• I want to see the INTRO VORTRANE paragraphs used. The main slogan to doctors is: Vortrane Global Compounding Pharmacy: Care Built Around You Care built around you and your Patients.
Should not have
• Don't use pictures Vortrane_420 and Vortrane_408. I have deleted both pictures from the brief

```html
<!DOCTYPE html>
<html lang="en">
<head>
<meta charset="utf-8">
<title>Vortrane Global Compounding Pharmacy – Bi-fold Brochure</title>
<link rel="stylesheet" href="https://fonts.googleapis.com/css2?family=Fira+Sans:wght@300;600;700;800&family=Open+Sans:wght@400;600&family=Archivo+Black&display=swap">
<style>
  :root {
    --navy: #0b1f8e;
    --navy-deep: #08187a;
    --teal: #22c2a2;
    --teal-light: #3fd4b6;
    --white: #ffffff;
    --paper: #eceeef;
    --ink: #1d1d1f;
    --stage: #c9c9c9;
    --outline: #1f3fd6;
  }
  * { box-sizing: border-box; margin: 0; padding: 0; }
  html, body { width: 924px; height: 1200px; overflow: hidden; background: var(--stage); }
  .canvas { position: relative; width: 924px; height: 1200px; }
  .page {
    position: absolute; top: 286px; width: 430px; height: 628px;
    overflow: hidden; box-shadow: 0 4px 14px rgba(0,0,0,.25);
    font-family: "Open Sans", sans-serif;
  }
  .page--cover { left: 20px; }
  .page--back { left: 474px; }
  .page__shapes { position: absolute; inset: 0; width: 100%; height: 100%; }

  .wordmark {
    position: absolute; font-family: "Fira Sans", sans-serif; font-weight: 300;
    color: var(--ink); letter-spacing: 1.5px; line-height: 1;
  }
  .page--cover .wordmark { right: 22px; top: 34px; font-size: 30px; }
  .page--back .wordmark { left: 262px; top: 445px; font-size: 20px; color: var(--white); }

  .cover-title {
    position: absolute; left: 29px; top: 446px;
    font-family: "Fira Sans", sans-serif; font-weight: 700; font-size: 31px; line-height: 38px;
  }
  .cover-title__lead { color: var(--teal); display: block; }
  .cover-title__main { color: var(--white); display: block; }
  .tagline {
    position: absolute; left: 29px; top: 528px; padding-left: 11px;
    border-left: 2px solid var(--teal);
    color: var(--white); font-size: 11.5px; line-height: 16px;
  }

  .site-url {
    position: absolute; left: 29px; top: 596px;
    font-size: 12px; letter-spacing: 4px; color: var(--ink);
  }
  .site-url__bar { position: absolute; left: 29px; top: 619px; width: 162px; height: 5px; background: var(--teal); }

  .intro-head {
    position: absolute; left: 32px; top: 24px; padding-left: 12px;
    border-left: 2px solid var(--white); color: var(--white);
  }
  .intro-head__title { font-family: "Fira Sans", sans-serif; font-weight: 700; font-size: 21px; line-height: 24px; margin-top: -4px; }
  .intro-head__slogan { font-size: 10px; line-height: 13.5px; margin-top: 6px; }

  .intro-body {
    position: absolute; left: 32px; top: 116px; width: 330px;
    font-size: 8.9px; line-height: 13.4px; color: var(--ink);
  }
  .intro-body p + p { margin-top: 13px; }

  .contact-icons { position: absolute; left: 32px; top: 440px; display: flex; gap: 4px; }
  .contact-details {
    position: absolute; left: 32px; top: 455px;
    font-size: 11.3px; line-height: 14.3px; color: var(--white);
  }
  .follow-us {
    position: absolute; left: 268px; top: 490px;
    font-family: "Fira Sans", sans-serif; font-weight: 600; font-size: 12px; color: var(--teal);
  }
  .contact-outline {
    position: absolute; left: 28px; top: 528px;
    font-family: "Archivo Black", sans-serif; font-size: 47px; line-height: 1;
    color: transparent; -webkit-text-stroke: 1px var(--outline); letter-spacing: -0.5px;
  }
</style>
</head>
<body>
<main class="canvas">

  <!-- Front cover -->
  <section class="page page--cover" aria-label="Front cover">
    <svg class="page__shapes" viewBox="0 0 675 985" preserveAspectRatio="none" aria-hidden="false">
      <defs>
        <linearGradient id="coverTeal" x1="0" y1="0" x2="1" y2="1">
          <stop offset="0" stop-color="#22c2a2"/><stop offset="1" stop-color="#3fd4b6"/>
        </linearGradient>
        <linearGradient id="labPhoto" x1="0" y1="0" x2="1" y2="1">
          <stop offset="0" stop-color="#d9dde2"/><stop offset=".55" stop-color="#9aa3ad"/><stop offset="1" stop-color="#5f6a76"/>
        </linearGradient>
      </defs>
      <rect width="675" height="985" fill="url(#coverTeal)"/>
      <polygon points="112,0 265,0 0,440 0,185" fill="#0b1f8e"/>
      <polygon points="0,450 8,437 8,590 0,600" fill="#e9ecee"/>
      <polygon points="265,0 675,0 675,148 176,148" fill="#ffffff"/>
      <polygon points="262,148 675,148 675,475 598,635 0,635 0,583" fill="url(#labPhoto)" role="img" aria-label="Photo: pharmacist in hairnet and mask filling capsules at a compounding machine"/>
      <rect x="0" y="635" width="675" height="285" fill="#0b1f8e"/>
      <rect x="0" y="920" width="675" height="65" fill="#ffffff"/>
    </svg>
    <div class="wordmark">VORTRANE</div>
    <h1 class="cover-title">
      <span class="cover-title__lead">Vortrane Global</span>
      <span class="cover-title__main">Compounding Pharmacy</span>
    </h1>
    <p class="tagline">Care Built Around You Care built around you and your Patients.</p>
    <div class="site-url">www.vortrane.example</div>
    <div class="site-url__bar"></div>
  </section>

  <!-- Back page -->
  <section class="page page--back" aria-label="Back page">
    <svg class="page__shapes" viewBox="0 0 672 983" preserveAspectRatio="none">
      <defs>
        <linearGradient id="bandTeal" x1="0" y1="0" x2="1" y2="0">
          <stop offset="0" stop-color="#22c2a2"/><stop offset="1" stop-color="#45d8bc"/>
        </linearGradient>
        <linearGradient id="bottlePhoto" x1="0" y1="0" x2="1" y2="1">
          <stop offset="0" stop-color="#e3e6e8"/><stop offset="1" stop-color="#c4cacf"/>
        </linearGradient>
      </defs>
      <rect width="672" height="983" fill="#eceeef"/>
      <rect width="672" height="148" fill="url(#bandTeal)"/>
      <polygon points="560,188 672,188 510,618 405,618" fill="url(#bottlePhoto)" role="img" aria-label="Photo: frosted medicine bottle with a pharmacy label"/>
      <polygon points="672,180 672,922 0,922 0,640 530,640" fill="#0b1f8e"/>
      <polygon points="672,260 672,922 560,922 560,560" fill="#0a1a80" opacity=".55"/>
      <rect x="0" y="922" width="672" height="61" fill="#ffffff"/>
    </svg>

    <header class="intro-head">
      <h2 class="intro-head__title">Intro Vortrane</h2>
      <p class="intro-head__slogan">Vortrane Global Compounding Pharmacy: Care Built Around You<br>Care built around you and your Patients.</p>
    </header>

    <div class="intro-body">
      <p>We believe every person in the world should have access to the best possible health care, which is why we offer a full range of pharmaceuticals at our compounding pharmacy. We know that each person is unique and deserves personalized care—that's why we work with you to create a solution that works for your patient's specific needs. Our pharmacists will work with you to understand your goals and provide a customized plan that will help you reach them. We know what it's like being a doctor today: You have so many responsibilities, so many patients who need your attention… and so many medications that don't always work!</p>
      <p>We know that as a doctor, you have a lot on your plate—and sometimes it can feel like there's no time left in the day to get things done. That's why we work with you directly to develop customized solutions that meet your needs and help you get more done. Whether you need a new drug or an injectable for one of your patients, we're here for you.</p>
      <p>Whether you're looking for something simple or something more complex, we're here to help make sure that everything gets done on time and according to your specifications—and at reasonable prices That's why we created this brochure: To make sure you know about all of the ways we can help.</p>
    </div>

    <div class="contact-icons" aria-hidden="true">
      <svg width="10" height="10" viewBox="0 0 10 10"><circle cx="5" cy="5" r="5" fill="#fff"/><path d="M5 2.2a1.8 1.8 0 0 1 1.8 1.8C6.8 5.4 5 7.6 5 7.6S3.2 5.4 3.2 4A1.8 1.8 0 0 1 5 2.2z" fill="#0b1f8e"/></svg>
      <svg width="10" height="10" viewBox="0 0 10 10"><circle cx="5" cy="5" r="5" fill="#fff"/><path d="M3.2 2.5l1 1-.5.8a3.5 3.5 0 0 0 2 2l.8-.5 1 1-.7.8C5 7.4 2.6 5 2.4 3.2z" fill="#0b1f8e"/></svg>
      <svg width="10" height="10" viewBox="0 0 10 10"><circle cx="5" cy="5" r="5" fill="#fff"/><rect x="2.4" y="3.2" width="5.2" height="3.6" fill="#0b1f8e"/><path d="M2.4 3.2L5 5.2 7.6 3.2" stroke="#fff" stroke-width=".6" fill="none"/></svg>
    </div>
    <address class="contact-details" style="font-style:normal">
      18 Meridian Avenue,<br>
      10450 Harbour District, Portvale<br>
      +00 120 5550190<br>
      contact@vortrane.example
    </address>

    <div class="wordmark">VORTRANE</div>
    <div class="follow-us">Follow Us</div>
    <div class="contact-outline">CONTACT US</div>

    <div class="site-url" style="top:598px">www.vortrane.example</div>
    <div class="site-url__bar" style="top:621px"></div>
  </section>

</main>
</body>
</html>
```